Essential oil label for bottles

Looking to modify our current logo and label design. It looks too simple. I will attach images of our competitors to use as examples. Our company name is Velnora. We have 2 different bottles. Clear and amber color. Going forward, we will be using only the amber bottle. The other 2 images are the biggest sellers brands. We want to make some adjustments to ours.

Target Market(s)

Brindex sales

Industry/Entity Type

Essential oil, perfume

Colors

Designer to choose only greyscale colors for use in the design.

Requirements
Nice to have
• A slight change to fonts and logo design. Maybe change the font and design of the word "Velnora" in our logo. Maybe add something to the label to make it stand out more but still keeping it clean and modern
Should not have
• No colors, besides, black, grays, whites, and off white.

```html
<!DOCTYPE html>
<html lang="en">
<head>
<meta charset="utf-8">
<title>Velnora Fragrance Oil Labels</title>
<link rel="stylesheet" href="https://fonts.googleapis.com/css2?family=Manrope:wght@700&family=Questrial&display=swap">
<style>
  :root {
    --paper: #f8f6f1;
    --ink: #141414;
    --label-dark: #111111;
    --label-light: #f1f1f1;
    --label-light-shade: #d6d6d6;
    --text-on-dark: #f2f2f2;
    --muted-on-dark: #c9c9c9;
    --muted-on-light: #6a6a6a;
    --tag-light: #cfcfcf;
    --code-area-dark: #3a3a3a;
    --code-area-light: #bdbdbd;
  }
  * { margin: 0; padding: 0; box-sizing: border-box; }
  html, body { width: 1200px; height: 800px; overflow: hidden; }
  body {
    background: var(--paper);
    font-family: "Questrial", sans-serif;
    position: relative;
  }
  .label {
    position: absolute;
    top: 351px;
    width: 166px;
    height: 241px;
  }
  .label--palosanto { left: 392px; background: var(--label-dark); color: var(--text-on-dark); }
  .label--whitetea {
    left: 613px;
    background: linear-gradient(90deg, var(--label-light) 0%, #ffffff 35%, var(--label-light-shade) 100%);
    color: var(--ink);
  }
  .label__brand {
    position: absolute; top: 20px; left: 20px;
    font-size: 10px; letter-spacing: 1px;
  }
  .label__name {
    position: absolute; top: 62px; left: 20px;
    font-family: "Manrope", sans-serif; font-weight: 700;
    font-size: 12.5px; letter-spacing: 0.3px;
  }
  .label__type {
    position: absolute; top: 116px; left: 20px;
    font-size: 7px; letter-spacing: 0.2px;
  }
  .label--palosanto .label__type { color: var(--muted-on-dark); }
  .label--whitetea .label__type { color: var(--muted-on-light); }
  .label__rule {
    position: absolute; top: 130px; left: 20px;
    width: 110px; height: 1px; background: currentColor; opacity: 0.8;
  }
  .label__notes {
    position: absolute; top: 136px; left: 20px;
    display: flex; align-items: center; gap: 2px;
    font-size: 6px; white-space: nowrap;
  }
  .note { padding: 1px 1px; }
  .note__divider { width: 1px; height: 8px; background: currentColor; }
  .label--palosanto .note--active { background: var(--tag-light); color: var(--ink); padding: 1px 2px; }
  .label--whitetea .note--active { background: var(--ink); color: #ffffff; padding: 1px 2px; }
  .label__code-area {
    position: absolute; top: 60px; left: 139px;
    width: 15px; height: 122px;
  }
  .label--palosanto .label__code-area { background: var(--code-area-dark); }
  .label--whitetea .label__code-area { background: var(--code-area-light); }
  .label__volume {
    position: absolute; top: 219px; left: 20px;
    font-size: 6.5px;
  }
  .wordmark {
    position: absolute; left: 880px; top: 494px;
    font-size: 40px; letter-spacing: 2px;
    color: var(--ink);
  }
</style>
</head>
<body>
  <section class="label label--palosanto">
    <div class="label__brand">Velnora</div>
    <h2 class="label__name">PALOSANTO</h2>
    <p class="label__type">FRAGRANCE OIL</p>
    <div class="label__rule"></div>
    <div class="label__notes">
      <span class="note">WHITETEA</span><span class="note__divider"></span><span class="note">ORANGE</span><span class="note note--active">PALOSANTO</span>
    </div>
    <div class="label__code-area" role="img" aria-label="Product code area"></div>
    <p class="label__volume">200 ML</p>
  </section>

  <section class="label label--whitetea">
    <div class="label__brand">Velnora</div>
    <h2 class="label__name">WHITETEA</h2>
    <p class="label__type">FRAGRANCE OIL</p>
    <div class="label__rule"></div>
    <div class="label__notes">
      <span class="note note--active">WHITETEA</span><span class="note">ORANGE</span><span class="note__divider"></span><span class="note">PALOSANTO</span>
    </div>
    <div class="label__code-area" role="img" aria-label="Product code area"></div>
    <p class="label__volume">200 ML</p>
  </section>

  <div class="wordmark">Velnora</div>
</body>
</html>
```